Energy Company needs a Business Card Design

We need a business card design for a new company based in Singapore called Tarn Energy. Tarn Energy is a producer of renewable energies largely for the biofuels market. Sourced entirely from sustainable resources, Tarn Energy aims to be a fully integrated oil company operating in 100% sustainable way. We would like to see designs that use the same colours as the attached file.

Industry/Entity Type

Business

```html
<!DOCTYPE html>
<html lang="en">
<head>
<meta charset="utf-8">
<title>Tarn Energy – Business Card</title>
<link rel="stylesheet" href="https://fonts.googleapis.com/css2?family=Questrial&family=Montserrat:wght@700&display=swap">
<style>
  :root {
    --backdrop: #e8e9ea;
    --card-top: #4a4b4d;
    --card-bottom: #2f3031;
    --brand-green: #7bbf3f;
    --mark-grey: #9b9c9d;
    --text-grey: #b4b5b6;
  }
  * { margin: 0; padding: 0; box-sizing: border-box; }
  html, body {
    width: 1200px; height: 720px; overflow: hidden;
    background: var(--backdrop);
  }
  .stage { position: relative; width: 1200px; height: 720px; }
  .card {
    position: absolute; top: 241px;
    width: 420px; height: 240px;
    background: linear-gradient(160deg, var(--card-top) 0%, var(--card-bottom) 75%);
    font-family: "Questrial", sans-serif;
  }
  .card--front { left: 147px; }
  .card--back { left: 633px; }

  .front-brand {
    position: absolute; left: 0; right: 0; top: 78px;
    display: flex; align-items: center; justify-content: center; gap: 10px;
  }
  .brand-name {
    font-family: "Questrial", sans-serif;
    color: var(--mark-grey);
    white-space: nowrap;
  }
  .front-brand .brand-name { font-size: 52px; line-height: 1; }
  .brand-dot {
    display: block; border-radius: 50%; background: var(--brand-green);
  }
  .front-brand .brand-dot { width: 16px; height: 16px; }
  .tagline {
    position: absolute; left: 0; right: 0; top: 182px;
    text-align: center; color: var(--brand-green); font-size: 15px;
  }

  .contact { position: absolute; left: 20px; top: 66px; }
  .person-name {
    font-family: "Montserrat", sans-serif; font-weight: 700;
    color: var(--brand-green); font-size: 15px; line-height: 1.1;
  }
  .person-role { color: var(--text-grey); font-size: 13px; line-height: 1.2; }
  .contact-list { list-style: none; margin-top: 22px; }
  .contact-list li {
    display: flex; align-items: center; gap: 8px;
    color: var(--text-grey); font-size: 12px; height: 20px;
  }
  .contact-list svg { width: 11px; height: 11px; flex: none; }

  .back-brand {
    position: absolute; right: 20px; top: 98px;
    display: flex; align-items: center; gap: 6px;
  }
  .back-brand .brand-name { font-size: 28px; line-height: 1; }
  .back-brand .brand-dot { width: 9px; height: 9px; }
</style>
</head>
<body>
<main class="stage">
  <section class="card card--front">
    <div class="front-brand">
      <span class="brand-name">Tarn Energy</span>
      <span class="brand-dot"></span>
    </div>
    <p class="tagline">Energy for Biofuels Market</p>
  </section>

  <section class="card card--back">
    <div class="contact">
      <p class="person-name">Reed Calloway</p>
      <p class="person-role">CEO</p>
      <ul class="contact-list">
        <li>
          <svg viewBox="0 0 12 12" aria-hidden="true"><rect x="3" y="0.5" width="6" height="11" rx="1" fill="none" stroke="var(--brand-green)" stroke-width="1"/><rect x="5" y="9.3" width="2" height="1" fill="var(--brand-green)"/></svg>
          + 65 548 2291
        </li>
        <li>
          <svg viewBox="0 0 12 12" aria-hidden="true"><rect x="0.5" y="2" width="11" height="8" fill="var(--brand-green)"/><path d="M0.5 2 L6 6.5 L11.5 2" fill="none" stroke="var(--card-bottom)" stroke-width="1"/></svg>
          hello@tarnfuel.com
        </li>
        <li>
          <svg viewBox="0 0 12 12" aria-hidden="true"><g fill="none" stroke="var(--brand-green)" stroke-width="0.9"><circle cx="6" cy="6" r="5.2"/><ellipse cx="6" cy="6" rx="2.3" ry="5.2"/><line x1="0.8" y1="6" x2="11.2" y2="6"/><line x1="1.6" y1="3.4" x2="10.4" y2="3.4"/><line x1="1.6" y1="8.6" x2="10.4" y2="8.6"/></g></svg>
          www.tarnenergy.com
        </li>
      </ul>
    </div>
    <div class="back-brand">
      <span class="brand-name">Tarn Energy</span>
      <span class="brand-dot"></span>
    </div>
  </section>
</main>
</body>
</html>
```